Professional Facebook Banner, Business Cards, Door Hang Tags, Service Flyer for Pest Control Company

There are really 4 things I need designed but Pixel Harbor doesn't have them to package together. I am needing to get a Professional Facebook Banner, Business Cards, Door Hang Tags, and Service Flyer for a Pest Control Company. I already have a logo that I will attach to the project along with content a for each one of these tasks. Please see document attached labeled All Design Content & Flyer Content.
Pest Control

```html
<!DOCTYPE html>
<html lang="en">
<head>
<meta charset="utf-8">
<title>Copper Grove Pest Control – Print &amp; Social Set</title>
<link rel="stylesheet" href="https://fonts.googleapis.com/css2?family=Montserrat:ital,wght@0,400;0,500;0,600;0,700;0,800;1,800&display=swap">
<style>
:root{
  --orange:#f26b1d;
  --orange-dark:#c9500f;
  --ink:#161616;
  --charcoal:#222326;
  --white:#ffffff;
  --paper:#fbfbfb;
  --stage:#e9e9ea;
  --muted:#9a9a9a;
}
*{box-sizing:border-box;margin:0;padding:0}
html,body{width:1200px;height:2172px;overflow:hidden}
body{background:var(--stage);font-family:"Montserrat",sans-serif;color:var(--ink);position:relative}
.abs{position:absolute}
.brand-name{font-family:"Montserrat",sans-serif;font-weight:800;color:var(--orange);letter-spacing:.5px;line-height:1.05}

/* check bullet */
.check{list-style:none}
.check li{position:relative;padding-left:19px;font-weight:600}
.check li::before{content:"";position:absolute;left:0;top:50%;width:11px;height:11px;margin-top:-6.5px;border:1.5px solid var(--orange);border-radius:50%}
.check li::after{content:"";position:absolute;left:3.5px;top:50%;width:3px;height:3px;margin-top:-2.5px;border-top:1.5px solid var(--orange);border-right:1.5px solid var(--orange);transform:rotate(45deg)}

/* ===== Flyer ===== */
.flyer{position:absolute;left:253px;top:32px;width:672px;height:942px;background:var(--paper);box-shadow:0 18px 30px rgba(0,0,0,.18);overflow:hidden}
.flyer .hero-art{position:absolute;left:0;top:0}
.flyer .logo{left:29px;top:52px;font-size:24px;width:320px}
.flyer .intro{left:29px;top:130px;width:282px;color:var(--white)}
.flyer .intro h1{font-size:19px;font-weight:800;line-height:1.15}
.flyer .intro .rule{width:34px;height:3px;background:var(--white);margin:12px 0 13px}
.flyer .intro p{font-size:10.2px;font-weight:500;line-height:13px;margin-bottom:8px}
.flyer .covered{left:29px;top:388px;width:614px;font-size:10.6px;font-weight:600;line-height:13.5px}
.flyer .covered b{color:var(--orange);font-weight:700}
.plan-head{position:absolute;height:27px;font-size:15.5px;font-weight:700;color:var(--white);padding-left:11px;line-height:27px;letter-spacing:.3px}
.plan-head.dark{background:var(--ink)}
.plan-head.lit{background:var(--orange)}
.plan-list{position:absolute;font-size:11.2px;line-height:18.5px}
.plan-list .extra{color:var(--orange);font-weight:700}
.price{position:absolute;height:20px;border-bottom:1.5px solid var(--ink)}
.price span{position:absolute;left:-19px;bottom:-4px;color:var(--orange);font-weight:700;font-size:16px}
.flyer .gold-photo{left:275px;top:718px;width:368px;height:143px;background:linear-gradient(120deg,#d9d9d9,#f1f1f1 55%,#c7ccd2)}
.flyer .note{left:0;top:911px;width:672px;height:31px;background:var(--orange);color:var(--white);font-size:6.6px;font-weight:500;padding:7px 29px 0;line-height:9px}

/* ===== Business cards ===== */
.card{position:absolute;left:40px;width:525px;height:300px;overflow:hidden;box-shadow:0 12px 24px rgba(0,0,0,.2)}
.card.front{top:1010px;background:var(--white)}
.card.back{top:1340px;background:var(--ink)}
.card .logo{left:26px;top:30px;font-size:24px;width:230px}
.card .person{right:28px;top:78px;text-align:right}
.card .person .name{color:var(--orange);font-size:22px;font-weight:800;letter-spacing:.5px}
.card .person .role{font-size:15px;font-weight:800;letter-spacing:.8px}
.card .contact-bar{left:0;top:140px;width:525px;height:38px;background:var(--ink);color:var(--white);display:flex;align-items:center;justify-content:space-around;font-size:10px;font-weight:500}
.card .contact-bar span{display:flex;align-items:center;gap:6px}
.card .contact-bar i{display:inline-block;width:13px;height:13px;border-radius:50%;background:var(--orange)}
.card .service-bar{left:0;top:178px;width:525px;height:30px;background:var(--orange);color:var(--white);font-weight:700;font-size:13px;line-height:30px;padding-left:26px}
.card .services{left:26px;top:222px;width:490px;display:grid;grid-template-columns:repeat(5,1fr);row-gap:14px;font-size:10px}
.card .services li{font-weight:500;white-space:nowrap}
.card.back .logo{left:0;top:0;width:525px;height:300px;display:flex;align-items:center;justify-content:center;font-size:30px;text-align:center}

/* ===== Door hangers ===== */
.hanger{position:absolute;top:1083px;width:212px;height:550px;background:var(--charcoal);border-radius:6px;overflow:hidden;box-shadow:0 12px 24px rgba(0,0,0,.2)}
.hanger.one{left:639px}
.hanger.two{left:906px}
.hanger .hole{position:absolute;left:64px;top:14px;width:84px;height:84px;border-radius:50%;background:var(--stage)}
.hanger .slit{position:absolute;left:140px;top:58px;width:72px;height:10px;background:var(--stage)}
.hanger .logo{left:0;top:118px;width:212px;text-align:center;font-size:13px}
.hanger .art{position:absolute;left:0;top:150px}
.hanger .body{position:absolute;left:0;top:305px;width:212px;height:205px;background:var(--white)}
.hanger .copy{position:absolute;left:11px;top:8px;width:192px;font-size:7.4px;line-height:9.4px;font-weight:500}
.hanger .copy p{margin-bottom:7px}
.hanger .offer{position:absolute;left:0;top:128px;width:212px;text-align:center}
.hanger .offer .pct{color:var(--orange);font-size:27px;font-weight:800;line-height:28px}
.hanger .offer .plan{font-size:10px;font-weight:700}
.hanger .offer .who{color:var(--orange);font-size:5.5px;font-weight:700;margin-top:1px}
.hanger .cta{position:absolute;left:10px;top:181px;width:192px;height:20px;background:var(--orange);color:var(--white);font-size:9.5px;font-weight:700;text-align:center;line-height:20px}
.hanger .foot{position:absolute;left:0;top:512px;width:212px;text-align:center;color:var(--white);font-size:9.5px;font-weight:600;line-height:14px}
.hanger .svc-head{position:absolute;left:10px;top:14px;width:192px;height:20px;background:var(--orange);color:var(--white);font-size:9.5px;font-weight:700;line-height:20px;padding-left:10px}
.hanger .svc{position:absolute;left:10px;top:44px;width:200px;display:grid;grid-template-columns:68px 64px 68px;row-gap:9px;font-size:7.8px}
.hanger .svc li{font-weight:500;white-space:nowrap}

/* ===== Cover banner ===== */
.banner{position:absolute;left:77px;top:1716px;width:1050px;height:398px;background:var(--ink);overflow:hidden;box-shadow:0 14px 26px rgba(0,0,0,.2)}
.banner .shapes{position:absolute;left:0;top:0}
.banner .crew{position:absolute;top:18px;height:380px;background:linear-gradient(180deg,#f4f4f4,#d8dade 70%,#b9bcc2)}
.banner .crew.left{left:40px;width:280px;border-radius:120px 120px 0 0}
.banner .crew.right{left:740px;width:280px;border-radius:120px 120px 0 0}
.banner .logo{left:300px;top:80px;width:450px;text-align:center;font-size:38px}
.banner .contact{left:300px;top:240px;width:450px;text-align:center;font-style:italic;font-weight:800}
.banner .contact .label{color:var(--orange);font-size:26px}
.banner .contact .phone{color:var(--white);font-size:35px;margin-top:2px}
</style>
</head>
<body>

<!-- Service flyer -->
<section class="flyer">
  <svg class="hero-art" width="672" height="380" viewBox="0 0 672 380">
    <defs>
      <linearGradient id="heroPhoto" x1="0" y1="0" x2="1" y2="1">
        <stop offset="0" stop-color="#2a3038"/>
        <stop offset=".5" stop-color="#cfd5dd"/>
        <stop offset="1" stop-color="#2a3038"/>
      </linearGradient>
    </defs>
    <polygon points="0,124 248,124 392,300 358,376 0,376" fill="var(--orange)"/>
    <polygon points="492,12 672,12 672,376 412,376 455,300 300,124 430,124" fill="#1d2128"/>
    <rect x="440" y="60" width="232" height="316" fill="url(#heroPhoto)" role="img" aria-label="Technician in white protective suit and respirator holding a sprayer"/>
  </svg>
  <div class="abs brand-name logo">COPPER GROVE<br>PEST CONTROL</div>
  <div class="abs intro">
    <h1>COPPER GROVE<br>PEST CONTROL</h1>
    <div class="rule"></div>
    <p>Pests are constantly trying to enter your home, which can easily cause frustration and damage to your home and belongings. That's why we at Copper Grove Pest Control provide seasonally designed, proactive home pest control plans to protect your family and your home.</p>
    <p>Our home pest control plans offer effective and affordable solutions to all your pest issues in and around your home. If you have pest problems, schedule your free inspection today!</p>
  </div>
  <p class="abs covered"><b>COVERED PESTS:</b> Ants, Carpenter Ants, Bees, Carpenter Bees, Box Elder Bugs, Centipedes, Clover Mites, Crickets, General Spiders, Ground Beetles, Earwigs, Millipedes, Mice, Oriental Roaches, Pill Bugs, Sow Bugs, Scorpions, and Wasps all within 10 feet of the structure being treated.</p>

  <div class="plan-head dark" style="left:29px;top:442px;width:300px">HOME DEFENSE BRONZE</div>
  <ul class="plan-list check" style="left:29px;top:474px">
    <li>Year-Round Pest Protection</li><li>Bi-Monthly Service (6 visits per year)</li><li>Covers 15+ Pests</li><li>Exterior Treatment</li><li>Interior Treatment (As Needed)</li><li>Rodent Control</li><li>Stinging Insect Removal</li><li>Free Re-Treatments</li>
  </ul>
  <div class="price" style="left:47px;top:643px;width:251px"><span>$</span></div>

  <div class="plan-head lit" style="left:343px;top:442px;width:300px">HOME DEFENSE SILVER</div>
  <ul class="plan-list check" style="left:343px;top:474px">
    <li>Year-Round Pest Protection</li><li>Bi-Monthly Service (6 visits per year)</li><li>Covers 15+ Pests</li><li>Exterior Treatment</li><li>Interior Treatment (As Needed)</li><li>Rodent Control</li><li>Stinging Insect Removal</li><li>Free Re-Treatments</li><li class="extra">+ TERMITE MONITORING</li>
  </ul>
  <div class="price" style="left:361px;top:643px;width:282px"><span>$</span></div>

  <div class="plan-head dark" style="left:29px;top:679px;width:614px">HOME DEFENSE GOLD</div>
  <ul class="plan-list check" style="left:29px;top:711px">
    <li>Year-Round Pest Protection</li><li>Bi-Monthly Service (6 visits per year)</li><li>Covers 15+ Pests</li><li>Exterior Treatment</li><li>Interior Treatment (As Needed)</li><li>Rodent Control</li><li>Stinging Insect Removal</li><li>Free Re-Treatments</li><li class="extra" style="line-height:16px">Termite Monitoring &amp;<br>Mosquito Reduction Treatments</li>
  </ul>
  <div class="abs gold-photo" role="img" aria-label="Technicians in protective suits and masks inside a home"></div>
  <div class="price" style="left:299px;top:875px;width:344px"><span>$</span></div>

  <p class="abs note">Please Note: to have full guarantee for Asian Beetles, Brown Recluse Spider, Cluster Flies, Lady Bugs, and Silverfish the structures attic and/or crawlspace would need to be treated. There are additional fees for theses services</p>
</section>

<!-- Business card front -->
<section class="card front">
  <div class="abs brand-name logo">COPPER GROVE PEST CONTROL</div>
  <div class="abs person"><div class="name">DALE MORGAN</div><div class="role">OWNER</div></div>
  <div class="abs contact-bar">
    <span><i></i>555-014-2290</span>
    <span><i></i>dale@coppergrovepest.com</span>
    <span><i></i>www.coppergrovepest.com</span>
  </div>
  <div class="abs service-bar">SERVICES / INSPECTIONS</div>
  <ul class="abs services check">
    <li>Ants</li><li>Mosquitos</li><li>Fleas</li><li>Roaches</li><li>Stinging Insects</li>
    <li>Spiders</li><li>Rodents</li><li>Termites</li><li>Mice</li><li>Rats</li>
  </ul>
</section>

<!-- Business card back -->
<section class="card back">
  <div class="abs brand-name logo">COPPER GROVE<br>PEST CONTROL</div>
</section>

<!-- Door hanger: introduction -->
<section class="hanger one">
  <div class="hole"></div><div class="slit"></div>
  <div class="abs brand-name logo">COPPER GROVE<br>PEST CONTROL</div>
  <svg class="art" width="212" height="160" viewBox="0 0 212 160">
    <rect x="0" y="8" width="212" height="152" fill="#b4521c" role="img" aria-label="Technicians in protective suits treating a home interior"/>
    <path d="M0 110 L78 152 Q106 168 134 150 L212 112 L212 160 L0 160Z" fill="var(--white)"/>
    <path d="M60 146 Q84 122 106 150 Q128 126 152 146" fill="none" stroke="var(--ink)" stroke-width="4"/>
  </svg>
  <div class="body">
    <div class="copy">
      <p>We are a locally owned and operated, with 10 years of industry experience our family is committed to delivering exceptional customer service and high-quality results. We strive for excellence in all that we do.</p>
      <p>We treat each and every customer like a member of our family. When you partner with us, you can enjoy hassle-free services, expert care, and peace of mind knowing you and your home are protected from pests for years to come.</p>
    </div>
    <div class="offer"><div class="pct">25%OFF</div><div class="plan">Initial Home Protection Plan</div><div class="who">NEW CUSTOMERS ONLY</div></div>
    <div class="cta">CALL NOW FOR A FREE QUOTE</div>
  </div>
  <div class="foot">(555) 014-2290<br>www.coppergrovepest.com</div>
</section>

<!-- Door hanger: services -->
<section class="hanger two">
  <div class="hole"></div><div class="slit"></div>
  <div class="abs brand-name logo">COPPER GROVE<br>PEST CONTROL</div>
  <svg class="art" width="212" height="160" viewBox="0 0 212 160">
    <rect x="0" y="8" width="212" height="152" fill="#a9470f" role="img" aria-label="Close-up of a gloved technician spraying treatment"/>
    <path d="M0 110 L78 152 Q106 168 134 150 L212 112 L212 160 L0 160Z" fill="var(--white)"/>
    <path d="M60 146 Q84 122 106 150 Q128 126 152 146" fill="none" stroke="var(--ink)" stroke-width="4"/>
  </svg>
  <div class="body">
    <div class="svc-head">OUR SERVICES</div>
    <ul class="svc check">
      <li>Termites</li><li>Spiders</li><li>Mosquitos</li>
      <li>Roaches</li><li>Ants</li><li>Rodents</li>
      <li>Fleas</li><li style="grid-column:span 2">StingingInsects</li>
      <li>&amp; More</li>
    </ul>
    <div class="offer"><div class="pct">25%OFF</div><div class="plan">One Time Service</div><div class="who">NEW CUSTOMERS ONLY</div></div>
    <div class="cta">CALL NOW FOR A FREE QUOTE</div>
  </div>
  <div class="foot">(555) 014-2290<br>www.coppergrovepest.com</div>
</section>

<!-- Social cover banner -->
<section class="banner">
  <svg class="shapes" width="1050" height="398" viewBox="0 0 1050 398">
    <path d="M0 0 L300 0 Q210 70 200 180 Q190 300 0 330Z" fill="var(--orange)"/>
    <path d="M230 398 Q300 290 400 330 Q450 355 455 398Z" fill="var(--orange)"/>
    <path d="M680 398 Q720 270 860 250 Q980 240 1050 150 L1050 398Z" fill="var(--orange)"/>
    <path d="M1050 0 L960 0 Q1030 60 1050 120Z" fill="var(--orange)"/>
  </svg>
  <div class="crew left" role="img" aria-label="Technician in white protective suit holding a fogging sprayer"></div>
  <div class="crew right" role="img" aria-label="Technician in protective suit and respirator with yellow gloves presenting the phone number"></div>
  <div class="abs brand-name logo">COPPER GROVE<br>PEST CONTROL</div>
  <div class="abs contact"><div class="label">CONTACT US</div><div class="phone">(555) 014-2290</div></div>
</section>

</body>
</html>
```